Certified Legal Nurse Consultant business needs a postcard design

Need a postcard that advertises to target market of attorneys. I am a registered nurse who helps lawyers with the medical issues on their cases. I want this card to highlight the benefit of my services versus the competition. Please see attached document for more info.
Updates

Reason: Many of the 20 designs I received were from the same designer, but just altered slightly. I was expecting ~20 original/unique designs. Thanks!

Target Market(s)

attorneys (lawyers)

Industry/Entity Type

Business

Font styles to use
Serif

Colors
3176b5
0355a3

Requirements
Must have
• my photo, business name and address, phone number, web address, description of how my business is better than the competition (see PDF file sent)

```html
<!DOCTYPE html>
<html lang="en">
<head>
<meta charset="utf-8">
<title>Harwell &amp; Associates – Postcard Design 02</title>
<link rel="stylesheet" href="https://fonts.googleapis.com/css2?family=Arimo:wght@400;700&family=Roboto+Condensed:wght@400;700&family=Cabin+Condensed:wght@400;600&display=swap">
<style>
:root{
  --board-light:#e8e8e8;
  --board-dark:#9c9c9c;
  --card-light:#dde0f0;
  --ink:#2a2a2a;
  --navy:#333d80;
  --royal:#2d4aa0;
  --accent:#3a62d8;
  --link:#4d70d6;
  --night:#0d0d16;
  --charcoal:#2e2e2e;
  --muted:#b9bcc6;
  --label:#555;
}
*{margin:0;padding:0;box-sizing:border-box}
html,body{width:1200px;height:1199px;overflow:hidden}
body{position:relative;background:radial-gradient(ellipse at 50% 45%,var(--board-light) 0%,#c9c9c9 55%,var(--board-dark) 100%);font-family:"Arimo",Arial,sans-serif;color:var(--ink)}
.abs{position:absolute}
.board-label{font-family:"Cabin Condensed",sans-serif;font-weight:600;font-size:33px;color:var(--label);letter-spacing:-.5px}
.card{position:absolute;top:89px;height:922px;box-shadow:0 6px 16px rgba(0,0,0,.35);overflow:hidden}

/* front */
.front{left:131px;width:463px;background:var(--night)}
.front-top{left:0;top:0;width:463px;height:107px;background:var(--card-light)}
.front-photo{left:0;top:107px;width:463px;height:474px;background:radial-gradient(ellipse at 55% 55%,#6b4a36 0%,#3a2a22 35%,#1c1a1c 70%,#121214 100%)}
.front-accent{left:0;top:107px;width:15px;height:50px;background:var(--accent)}
.front-name{right:44px;top:32px;font-size:70px;color:#111;line-height:1}
.front-llc{right:46px;top:115px;font-size:42px;color:#fff;line-height:1}
.front-banner{left:15px;top:581px;width:448px;height:58px;background:var(--royal);color:#fff;font-family:"Roboto Condensed",sans-serif;font-size:31px;line-height:58px;text-align:center}
.front-list{left:72px;top:669px;list-style:none;font-family:"Roboto Condensed",sans-serif;font-size:22px;line-height:28px;color:var(--muted)}
.front-list li{position:relative;padding-left:38px}
.tick{position:absolute;left:0;top:6px;width:18px;height:16px}
.front-url{left:0;top:857px;width:463px;height:65px;background:#08080f;color:var(--link);font-family:"Roboto Condensed",sans-serif;font-size:33px;line-height:65px;text-align:center}

/* back */
.back{left:644px;width:462px;background:var(--card-light)}
.back-title{left:0;top:30px;width:462px;text-align:center;font-size:33px;color:#333;line-height:1}
.back-sub{left:0;top:70px;width:462px;text-align:center;font-size:24px;color:#444;line-height:1}
.nurse-art{left:36px;top:133px;width:94px;height:132px;border-radius:40px 40px 20px 20px;background:linear-gradient(#2d2d3a 0%,#2d2d3a 45%,#4a5cb0 70%,#3d4d9c 100%)}
.about-head{left:137px;top:126px;font-size:24px;color:var(--navy)}
.about-text{left:135px;top:156px;width:294px;font-size:17px;line-height:21px;text-align:justify;color:#222}
.benefits{left:0;top:282px;width:462px;height:201px;background:var(--navy);color:#fff}
.benefits h2{position:absolute;left:50px;top:12px;font-size:23px;font-weight:400}
.check-list{list-style:none}
.check-list li{position:relative;padding-left:22px}
.check-list .tick{top:4px;width:13px;height:12px}
.benefits .check-list{position:absolute;left:49px;top:46px;width:400px;font-size:18px;line-height:21px}
.guarantee{position:absolute;left:0;top:169px;width:462px;text-align:center;font-weight:700;font-size:21px}
.services-head{left:49px;top:509px;font-size:23px;color:#333}
.services{left:49px;top:544px;font-size:19px;line-height:22px;color:#333;width:400px}
.contact-head{left:91px;top:702px;font-size:23px;color:#222}
.contact-band{left:0;top:734px;width:462px;height:188px;background:var(--charcoal);color:#fff}
.phone-icon{left:96px;top:26px;width:22px;height:26px}
.phone{left:127px;top:24px;font-size:24px;font-weight:700}
.address{left:127px;top:57px;font-size:18px;line-height:23px;color:#eee}
.mail-icon{left:95px;top:141px;width:22px;height:16px}
.email{left:127px;top:136px;font-size:20px}

/* board captions */
.plate{left:0;top:1035px;width:343px;height:84px;background:#1a1a1a}
.plate-text{left:53px;top:22px;font-family:"Cabin Condensed",sans-serif;font-size:32px;color:#fff}
.plate-num{left:288px;top:8px;font-family:"Cabin Condensed",sans-serif;font-size:38px;color:#2f6ee8}
.spec{left:55px;top:1134px;font-family:"Cabin Condensed",sans-serif;font-size:28px;color:#333}
.note{left:470px;top:1045px;width:650px;font-family:"Cabin Condensed",sans-serif;font-size:21px;line-height:25px;color:#333;letter-spacing:-.3px}
.note b{font-weight:600}
</style>
</head>
<body>
<svg width="0" height="0" style="position:absolute">
  <defs>
    <symbol id="tick" viewBox="0 0 18 16"><path d="M1 9 L6 14 L17 1" fill="none" stroke="currentColor" stroke-width="2"/></symbol>
  </defs>
</svg>

<div class="abs board-label" style="left:152px;top:36px">Front</div>
<div class="abs board-label" style="left:644px;top:38px">Back (option 02 - similar to flyer)</div>

<section class="card front">
  <div class="abs front-top"></div>
  <div class="abs front-photo" role="img" aria-label="Portrait photo of the nurse consultant in a dark blazer"></div>
  <div class="abs front-accent"></div>
  <div class="abs front-name">M. Harwell</div>
  <div class="abs front-llc">&amp; Associates, LLC</div>
  <div class="abs front-banner">Certified Legal Nurse Consulting</div>
  <ul class="abs front-list">
    <li><svg class="tick" style="color:var(--accent)"><use href="#tick"/></svg>Screen cases for merit</li>
    <li><svg class="tick" style="color:var(--accent)"><use href="#tick"/></svg>Develop medical summaries</li>
    <li><svg class="tick" style="color:var(--accent)"><use href="#tick"/></svg>Research authoritative literature</li>
    <li><svg class="tick" style="color:var(--accent)"><use href="#tick"/></svg>Locate testifying experts</li>
    <li><svg class="tick" style="color:var(--accent)"><use href="#tick"/></svg>Identify adherences to and<br>deviations from standard of care</li>
  </ul>
  <div class="abs front-url">www.harwell-associates.com</div>
</section>

<section class="card back">
  <div class="abs back-title">M. Harwell &amp; Associates</div>
  <div class="abs back-sub">Certified Legal Nurse Consultant</div>
  <div class="abs nurse-art" role="img" aria-label="Illustration of a nurse in cap and blue uniform"></div>
  <div class="abs about-head">About us</div>
  <p class="abs about-text">as a Certified Legal Nurse Consultant (CLNC) and Registered Nurse (RN) with over 26 years experience, I help attorneys effectively develop the medical-related issues in their cases.</p>

  <div class="abs benefits">
    <h2>What are the benefits?</h2>
    <ul class="check-list">
      <li><svg class="tick" style="color:#fff"><use href="#tick"/></svg>Saves time and money</li>
      <li><svg class="tick" style="color:#fff"><use href="#tick"/></svg>Bring healthcare expertise to the case development</li>
      <li><svg class="tick" style="color:#fff"><use href="#tick"/></svg>Frees up attorney time to focus on legal matters, while CLNC addresses medical issues</li>
    </ul>
    <div class="guarantee">100% risk free guarantee on work product</div>
  </div>

  <div class="abs services-head">CLNC services provided</div>
  <ul class="abs check-list services">
    <li><svg class="tick" style="color:var(--navy)"><use href="#tick"/></svg>Screen cases for merit</li>
    <li><svg class="tick" style="color:var(--navy)"><use href="#tick"/></svg>Develop medical summaries</li>
    <li><svg class="tick" style="color:var(--navy)"><use href="#tick"/></svg>Research authoritative literature</li>
    <li><svg class="tick" style="color:var(--navy)"><use href="#tick"/></svg>Locate testifying experts</li>
    <li><svg class="tick" style="color:var(--navy)"><use href="#tick"/></svg>Identify adherences to and deviations from standard of care</li>
  </ul>

  <div class="abs contact-head">Contact</div>
  <div class="abs contact-band">
    <svg class="abs phone-icon" viewBox="0 0 22 26"><path d="M5 2 L9 7 L7 10 Q9 15 13 18 L16 16 L20 20 L17 24 Q8 22 3 10 Q2 5 5 2Z" fill="none" stroke="#fff" stroke-width="2"/></svg>
    <div class="abs phone">(555) 014-2290</div>
    <div class="abs address">M. Harwell &amp; Associates LLC<br>1820 Meadowlark Lane<br>Cedar Bluff, MN 55000</div>
    <svg class="abs mail-icon" viewBox="0 0 22 16"><rect x="1" y="1" width="20" height="14" fill="none" stroke="#fff" stroke-width="2"/><path d="M1 1 L11 9 L21 1 M1 15 L8 7 M21 15 L14 7" fill="none" stroke="#fff" stroke-width="2"/></svg>
    <div class="abs email">anna@harwell-associates.com</div>
  </div>
</section>

<div class="abs plate">
  <div class="abs plate-text">Postcard Design</div>
  <div class="abs plate-num">02</div>
</div>
<div class="abs spec">140 x 279 mm &nbsp;|&nbsp; Portrait Orientation</div>
<p class="abs note"><b>Please note:</b> Seeing that 140 x 279mm is not a standard US mail postcard size, I tried to provide the best solution to present the content, suggesting a flyer look. Thanks for the opportunity. Feedback is always appreciated.</p>
</body>
</html>
```